Paper and board wholesaler needs business card design for managers

We need a business card design that incorporates bordo red, white and/ or grey colors. The business card has to have our "VELON" logo and our partners paper group logo that we are part of - "ROSKU group". Both of the logos should be applied to the business card according to the guidelines for the usage of the logo that have been added in the uploaded files.
The letters (information on the card) should be easily readable, so no "shiny" or "glossy" text.
Besides the two logos, the business card needs to contain information for the respective person:
1) Name, Surname,
2) Job position (e.g. "sales represantative"),
3) E-mail,
4) Phone number,
5) text: "Kartonu Mājvieta (VELON)" LTD
6) our office address "Riga, Sārtaines street 42".
(also could have) 7) our homepage address "www.velon.lv"
Holiday season, so have a lot of tasks to take care of and not as much time to check SketchHarbor as often.
1) Name, Surname, 2) Job position (e.g. "sales represantative"), 3) E-mail, 4) Phone number, 5) text: "Kartonu Mājvieta (VELON)" LTD 6) our office address "Riga, Sārtaines street 42". (also could have) 7) our homepage address "www.velon.lv"
Other font styles liked:
- Josefin Sans

```html
<!DOCTYPE html>
<html lang="en">
<head>
<meta charset="utf-8">
<title>VELON business card</title>
<link href="https://fonts.googleapis.com/css2?family=Josefin+Sans:wght@300;400;600;700&display=swap" rel="stylesheet">
<style>
  :root {
    --backdrop: #151515;
    --card: #242424;
    --bordo: #913338;
    --white: #f2f2f2;
    --font: "Josefin Sans", sans-serif;
  }
  * { margin: 0; padding: 0; box-sizing: border-box; }
  html, body {
    width: 1200px; height: 1156px; overflow: hidden;
    background: var(--backdrop);
    font-family: var(--font);
  }
  .card {
    position: absolute; left: 220px;
    width: 760px; height: 470px;
    background: var(--card);
    box-shadow: 0 10px 30px rgba(0,0,0,.5);
  }
  .card--front { top: 80px; }
  .card--back { top: 606px; }

  .brand {
    position: absolute; display: flex; align-items: center; gap: 22px;
    color: var(--bordo); font-weight: 600;
  }
  .brand__mark { width: 64px; height: 64px; border: 3px solid var(--bordo); }
  .brand__name { font-size: 30px; letter-spacing: 34px; }
  .card--front .brand { right: 56px; top: 120px; }

  .contact { position: absolute; left: 56px; top: 232px; }
  .contact__name {
    color: var(--bordo); font-weight: 600; font-size: 24px; letter-spacing: 1px;
  }
  .contact__role { color: var(--white); font-size: 17px; font-weight: 300; margin-top: 4px; }
  .contact__rule { width: 44px; height: 4px; background: var(--bordo); margin: 10px 0 20px; }
  .contact__list { list-style: none; }
  .contact__item {
    display: flex; align-items: center; gap: 12px;
    color: var(--white); font-size: 19px; font-weight: 300; margin-bottom: 12px;
  }
  .contact__item svg { width: 18px; height: 18px; fill: none; stroke: var(--bordo); stroke-width: 1.8; }

  .office {
    position: absolute; right: 56px; bottom: 48px; text-align: right;
  }
  .office__company { color: var(--bordo); font-weight: 600; font-size: 18px; }
  .office__address { color: var(--white); font-weight: 300; font-size: 18px; margin-top: 6px; }
  .office__web { color: var(--bordo); font-weight: 400; font-size: 18px; margin-top: 6px; }

  .card--back .brand { left: 80px; top: 90px; }
  .partner {
    position: absolute; left: 80px; bottom: 90px;
    display: flex; align-items: center; gap: 22px;
    color: var(--bordo); font-weight: 600;
  }
  .partner__mark { width: 74px; height: 74px; border-radius: 50%; border: 3px solid var(--bordo); }
  .partner__name { font-size: 60px; line-height: 1; }
</style>
</head>
<body>
  <section class="card card--front">
    <div class="brand">
      <span class="brand__mark"></span>
      <span class="brand__name">VELON</span>
    </div>

    <div class="contact">
      <p class="contact__name">EDGARS LANKO</p>
      <p class="contact__role">sales represantative</p>
      <div class="contact__rule"></div>
      <ul class="contact__list">
        <li class="contact__item">
          <svg viewBox="0 0 18 18"><rect x="4" y="1" width="10" height="16" rx="2"/><line x1="7" y1="14" x2="11" y2="14"/></svg>
          855-555-0142
        </li>
        <li class="contact__item">
          <svg viewBox="0 0 18 18"><path d="M4 2 l3 3 -2 2 c1 3 3 5 6 6 l2-2 3 3 -2 2 C8 16 2 10 2 4 Z"/></svg>
          855-555-0187
        </li>
        <li class="contact__item">
          <svg viewBox="0 0 18 18"><rect x="1.5" y="4" width="15" height="10"/><path d="M1.5 4 L9 10 L16.5 4"/></svg>
          edgars@velon.lv
        </li>
      </ul>
    </div>

    <div class="office">
      <p class="office__company">Kartonu Mājvieta (VELON) LTD</p>
      <p class="office__address">Riga, Sārtaines street 42, LV-1019, Latvia</p>
      <p class="office__web">www.velon.lv</p>
    </div>
  </section>

  <section class="card card--back">
    <div class="brand">
      <span class="brand__mark"></span>
      <span class="brand__name">VELON</span>
    </div>
    <div class="partner">
      <span class="partner__mark"></span>
      <span class="partner__name">ROSKU group</span>
    </div>
  </section>
</body>
</html>
```